Startup fashion company needs high-end, stylish and hip business cards!

We need a business card design that uses a logo that we just completed with a ArtFolkHub artist.

Our company is Velmora. We work with fashion designers to display their designs on our website and handle all back-end fulfillment for them (fabric sourcing, garment manufacturing, customer service, etc.). The word Velmora is a play on fashion trunk shows, where designers will show their wares in a small, intimate setting. The final design should communicate high-end / luxe, chic, stylish, fashion-forward, hip!

We are using greys as our logo color (#2d2d2d, #ababab). We are also interested, for branding purposes and on our website, to use purple as a highlight color (#4a3455). I have the logo in other formats if needed.

Target Market(s)

Investors, customers, fashion designers, suppliers

Industry/Entity Type

Fashion

Contact Information for Business Card

There should be space for:
Name
Title
Address 1
Address 2
City, State Zip
USA
Phone
Email
Skype
Twitter

If it makes sense to put one or more of the contact info on the same line, that is fine if it won't be confusing.

Font styles to use
Sans Serif
Other font styles liked:
• Would like the font to be complementary to our logo font/look and feel. The logo font is Caviar Dreams with a stylized 'N' according to the logo designer.

Colors
876aae
e4daea
f3f1f8
ffffff

Requirements
Must have
• The cards will most likely printed through PrintQuay and therefore must meet their upload file guidelines. There are also software templates for business cards that can be utilized. Information below from PrintQuay site.
• We support a variety of file formats for uploaded designs.
• Adobe Acrobat 9 Document (*.pdf) (recommended)
• Adobe Illustrator CS3 Artwork (*.ai) (recommended)
• Adobe Photoshop CS3 Image (*.psd) (recommended)
• Bitmap Image (*.bmp)
• GIF Image (*.gif)
• JPEG Image (*.jpg,*.jpeg)
• Microsoft PowerPoint 2010 Document (*.ppt)
• Microsoft Publisher 2010 Document (*.pub)
• Microsoft Word 2010 Document (*.doc)
• PCX Image (*.pcx)
• PICT Image (*.pic,*.pict,*.pct)
• PNG Image (*.png)
• PostScript Document (*.ps)
• TIFF Image (*.tif,*.tiff)
• Windows Enhanced Metafile (*.emf)
• Windows Metafile (*.wmf)
• The templates on their site:
• Using a downloadable template for your application will ensure that your dimensions, resolution and color settings match ours.
• - Adobe Photoshop (recommended) Download Horizontal Template
• - Adobe Illustrator (recommended) Download Horizontal Template
• If you are creating a PDF document in Acrobat Distiller, please use our Distiller settings.
• - Adobe Acrobat Distiller (recommended) Download Settings
• Sizing:
• Full Bleed Size
• 3.62" x 2.12"
• 92 x 54 mm
• 1085 x 635 pixels
• Document Trim Size
• 3.50" x 2.00"
• 89 x 51 mm
• 1050 x 600 pixels
Nice to have
• The back can use either the full logo or just the elephant or a combination? I'm imagining a full color backside...open to other suggestions!

```html
<!DOCTYPE html>
<html lang="en">
<head>
<meta charset="utf-8">
<title>Velmora Business Card</title>
<link rel="stylesheet" href="https://fonts.googleapis.com/css2?family=Josefin+Sans:wght@400&family=Open+Sans:wght@400;600&display=swap">
<style>
  :root {
    --page: #e9e7ec;
    --card: #f4f4f5;
    --card-edge: #ffffff;
    --ink: #2d2d2d;
    --dark: #1b2024;
    --purple: #4a3455;
    --white: #ffffff;
    --muted: #d6d8da;
  }
  html, body {
    margin: 0;
    padding: 0;
    width: 1200px;
    height: 899px;
    overflow: hidden;
    background: var(--page);
  }
  .canvas {
    position: relative;
    width: 1200px;
    height: 899px;
  }
  .card {
    position: absolute;
    left: 260px;
    width: 680px;
    height: 389px;
    background: radial-gradient(ellipse at 60% 45%, var(--card-edge), var(--card) 70%, #e6e6e8);
    box-shadow: 0 6px 18px rgba(0,0,0,0.18);
    overflow: hidden;
  }
  .card--front { top: 40px; }
  .card--back  { top: 470px; }

  .logo {
    position: absolute;
    display: flex;
    align-items: center;
    gap: 10px;
  }
  .logo__dot {
    width: 34px;
    height: 34px;
    border-radius: 50%;
    background: var(--purple);
  }
  .logo__name {
    font-family: "Josefin Sans", sans-serif;
    font-weight: 400;
    font-size: 40px;
    letter-spacing: 2px;
    color: var(--ink);
    line-height: 1;
    padding-top: 6px;
  }
  .card--front .logo { left: 50%; top: 50%; transform: translate(-50%, -50%); }
  .card--back .logo { left: 360px; top: 72px; }

  .back-art {
    position: absolute;
    inset: 0;
    width: 680px;
    height: 389px;
  }

  .holder {
    position: absolute;
    left: 40px;
    top: 44px;
    font-family: "Open Sans", sans-serif;
    color: var(--white);
  }
  .holder__name { font-weight: 600; font-size: 19px; margin: 0; }
  .holder__title { font-weight: 400; font-size: 15px; margin: 2px 0 0; color: var(--muted); }

  .contacts {
    position: absolute;
    left: 40px;
    bottom: 28px;
    margin: 0;
    padding: 0;
    list-style: none;
    font-family: "Open Sans", sans-serif;
    font-size: 11.5px;
    line-height: 19px;
    color: var(--muted);
  }
  .contacts li { display: flex; align-items: flex-start; gap: 7px; }
  .contacts svg { flex: none; margin-top: 4px; }
</style>
</head>
<body>
<main class="canvas">

  <section class="card card--front" aria-label="Card front">
    <div class="logo">
      <span class="logo__dot"></span>
      <span class="logo__name">VELMORA</span>
    </div>
  </section>

  <section class="card card--back" aria-label="Card back">
    <svg class="back-art" viewBox="0 0 680 389" aria-hidden="true">
      <path d="M0,0 L262,0 C212,60 208,140 258,200 C305,258 345,325 366,389 L0,389 Z" fill="var(--dark)"/>
      <path d="M276,0 C226,60 222,140 272,200 C319,258 359,325 380,389" fill="none" stroke="var(--purple)" stroke-width="5"/>
    </svg>

    <div class="holder">
      <p class="holder__name">Jordan Hale</p>
      <p class="holder__title">Owner / C.E.O</p>
    </div>

    <ul class="contacts">
      <li>
        <svg width="11" height="11" viewBox="0 0 12 12"><circle cx="6" cy="6" r="6" fill="var(--muted)"/><path d="M3 6.5 L6 3.5 L9 6.5 V9 H3 Z" fill="var(--dark)"/></svg>
        <span>Suite # 410, Elm Bldg,<br>NY 10014</span>
      </li>
      <li>
        <svg width="11" height="11" viewBox="0 0 12 12"><circle cx="6" cy="6" r="6" fill="var(--muted)"/><path d="M4 3 Q3 6 6 9 L8 8 L7 6.5 L6 7 Q5 6 5 5 L5.5 4 Z" fill="var(--dark)"/></svg>
        <span>212-555-0148</span>
      </li>
      <li>
        <svg width="11" height="11" viewBox="0 0 12 12"><circle cx="6" cy="6" r="6" fill="var(--muted)"/><rect x="4.2" y="2.5" width="3.6" height="7" rx="0.8" fill="var(--dark)"/></svg>
        <span>646-555-0193</span>
      </li>
      <li>
        <svg width="11" height="11" viewBox="0 0 12 12"><circle cx="6" cy="6" r="6" fill="var(--muted)"/><rect x="3" y="4" width="6" height="4.5" fill="var(--dark)"/></svg>
        <span>917-555-0126</span>
      </li>
      <li>
        <svg width="11" height="11" viewBox="0 0 12 12"><circle cx="6" cy="6" r="6" fill="var(--muted)"/><rect x="3" y="4" width="6" height="4" fill="var(--dark)"/><path d="M3 4 L6 6.3 L9 4" fill="none" stroke="var(--muted)" stroke-width="0.7"/></svg>
        <span>jordan@velmorahq.com</span>
      </li>
      <li>
        <svg width="11" height="11" viewBox="0 0 12 12"><circle cx="6" cy="6" r="6" fill="var(--muted)"/><circle cx="6" cy="6" r="3" fill="none" stroke="var(--dark)" stroke-width="0.9"/><path d="M3 6 H9 M6 3 V9" stroke="var(--dark)" stroke-width="0.7"/></svg>
        <span>www.velmorahq.com</span>
      </li>
    </ul>

    <div class="logo">
      <span class="logo__dot"></span>
      <span class="logo__name">VELMORA</span>
    </div>
  </section>

</main>
</body>
</html>
```